Upgrade UI for an existing app

I have an app that is already in the appstore, and I have finally get to the point where the app is fairly complete in its user flow and app features.

I would like to take the app to the next level, and completely revamp its look and feel, to give it that flat iOS7 look.

The app can be downloaded at https://apps.vendrulo.example/us/app/brindle-kto/id574093186?mt=8

And you can log into the app using the credential below:

sketch.harbor
password

I am also open to new ideas around UX, but my biggest focus is on getting the UI updated, especially for the setting page, support page, and about page.

Thanks,

Rob

Majority of the submissions are for iPhone, whereas I was hoping for more iPad redesign.

I think the issue is that, a lot of people didn't download the app from appstore.

I have uploaded two zip files with iPad screenshot.  Please submit a few designs that are based off the existing iPad screenshot.

```html
<!DOCTYPE html>
<html lang="en">
<head>
<meta charset="utf-8">
<title>My Exams</title>
<link rel="stylesheet" href="https://fonts.googleapis.com/css2?family=Roboto:wght@300;400;500&display=swap">
<style>
  :root {
    --header-blue: #08bdf7;
    --page-top: #dbe7ed;
    --page-bottom: #cad9e4;
    --card: #ffffff;
    --card-line: #dfe4e8;
    --title-ink: #2b3a48;
    --sub-ink: #b2b9bf;
    --pct-red: #ec1a4e;
    --ring-track: #ececec;
    --ring-green: #2fcf0a;
    --ring-lime: #d9f300;
    --icon-blue: #22a9ea;
    --white: #ffffff;
  }
  * { box-sizing: border-box; margin: 0; padding: 0; }
  html, body { width: 676px; height: 1200px; overflow: hidden; background: var(--page-bottom); }
  body { font-family: "Roboto", "Helvetica Neue", Arial, sans-serif; }
  .screen {
    width: 640px; height: 1136px; position: relative; overflow: hidden;
    transform: scale(1.05625); transform-origin: 0 0;
    background: linear-gradient(180deg, var(--page-top), var(--page-bottom));
  }
  .app-header {
    position: absolute; left: 0; top: 0; width: 640px; height: 128px;
    background: var(--header-blue); color: var(--white);
  }
  .status-bar {
    height: 40px; display: flex; align-items: center; justify-content: space-between;
    padding: 0 12px; font-size: 22px; font-weight: 400; position: relative;
  }
  .carrier { display: flex; align-items: center; gap: 6px; }
  .signal { font-size: 14px; letter-spacing: 1px; }
  .clock { position: absolute; left: 0; right: 0; text-align: center; font-weight: 500; pointer-events: none; }
  .power { display: flex; align-items: center; gap: 8px; }
  .battery { width: 44px; height: 20px; border: 2px solid var(--white); border-radius: 4px; padding: 2px; position: relative; }
  .battery::before { content: ""; display: block; width: 100%; height: 100%; background: var(--white); border-radius: 1px; }
  .battery::after { content: ""; position: absolute; right: -6px; top: 5px; width: 3px; height: 7px; background: var(--white); border-radius: 0 2px 2px 0; }
  .menu-button { position: absolute; left: 24px; top: 58px; width: 50px; height: 50px; }
  .screen-title {
    position: absolute; left: 0; right: 0; top: 56px; text-align: center;
    font-size: 40px; font-weight: 300; letter-spacing: 0.3px;
  }
  .exam-list { position: absolute; left: 27px; top: 160px; width: 586px; list-style: none; }
  .exam-card {
    height: 102px; margin-bottom: 30px; background: var(--card); border-radius: 51px;
    position: relative; box-shadow: 0 2px 2px rgba(80, 110, 130, 0.18);
  }
  .progress-ring { position: absolute; left: 8px; top: 7px; width: 88px; height: 88px; }
  .progress-ring text { font-family: "Roboto", "Helvetica Neue", Arial, sans-serif; font-size: 17px; fill: var(--pct-red); }
  .exam-title { position: absolute; left: 121px; top: 12px; font-size: 24px; font-weight: 400; color: var(--title-ink); white-space: nowrap; }
  .exam-status { position: absolute; left: 121px; top: 46px; font-size: 19px; font-weight: 300; color: var(--sub-ink); white-space: nowrap; }
  .exam-action {
    position: absolute; right: 0; top: 0; width: 90px; height: 102px;
    border-left: 1px solid var(--card-line); display: flex; align-items: center; justify-content: center;
  }
</style>
</head>
<body>
<svg width="0" height="0" style="position:absolute" aria-hidden="true">
  <defs>
    <linearGradient id="ring-fill" x1="0" y1="1" x2="1" y2="0">
      <stop offset="0" stop-color="var(--ring-green)"/>
      <stop offset="1" stop-color="var(--ring-lime)"/>
    </linearGradient>
    <g id="ring-base">
      <circle cx="44" cy="44" r="43" fill="var(--ring-track)"/>
      <circle cx="44" cy="44" r="35" fill="var(--white)"/>
    </g>
  </defs>
</svg>

<div class="screen">
  <header class="app-header">
    <div class="status-bar">
      <span class="carrier"><span class="signal">●●●○○</span> LUMA
        <svg width="22" height="16" viewBox="0 0 22 16"><path d="M1 5a14 14 0 0 1 20 0M4.5 8.5a9 9 0 0 1 13 0M8 12a4 4 0 0 1 6 0" fill="none" stroke="#fff" stroke-width="2.2" stroke-linecap="round"/><circle cx="11" cy="14.5" r="1.4" fill="#fff"/></svg>
      </span>
      <span class="clock">4:21 PM</span>
      <span class="power">100% <span class="battery"></span></span>
    </div>
    <svg class="menu-button" viewBox="0 0 50 50" aria-label="Menu" role="img">
      <circle cx="25" cy="25" r="23" fill="none" stroke="#fff" stroke-width="2"/>
      <path d="M17 19h16M17 25h16M17 31h16" stroke="#fff" stroke-width="2" stroke-linecap="round"/>
    </svg>
    <h1 class="screen-title">My Exams</h1>
  </header>

  <ul class="exam-list">
    <li class="exam-card">
      <svg class="progress-ring" viewBox="0 0 88 88"><use href="#ring-base"/><circle cx="44" cy="44" r="39" fill="none" stroke="url(#ring-fill)" stroke-width="7" stroke-dasharray="29.4 245" transform="rotate(-90 44 44)"/><text x="44" y="50" text-anchor="middle">12%</text></svg>
      <h2 class="exam-title">Skin and Soft Tissue</h2>
      <p class="exam-status">15 of 125 answered</p>
      <div class="exam-action"><svg width="20" height="32" viewBox="0 0 20 32"><path d="M3 2l14 14L3 30" fill="none" stroke="var(--icon-blue)" stroke-width="2"/></svg></div>
    </li>
    <li class="exam-card">
      <svg class="progress-ring" viewBox="0 0 88 88"><use href="#ring-base"/><circle cx="44" cy="44" r="39" fill="none" stroke="url(#ring-fill)" stroke-width="7"/><text x="44" y="50" text-anchor="middle">100%</text></svg>
      <h2 class="exam-title">Self-Assesstment 2006</h2>
      <p class="exam-status">Submitted</p>
      <div class="exam-action"><svg width="20" height="32" viewBox="0 0 20 32"><path d="M3 2l14 14L3 30" fill="none" stroke="var(--icon-blue)" stroke-width="2"/></svg></div>
    </li>
    <li class="exam-card">
      <svg class="progress-ring" viewBox="0 0 88 88"><use href="#ring-base"/><circle cx="44" cy="44" r="39" fill="none" stroke="url(#ring-fill)" stroke-width="7" stroke-dasharray="122.5 245" transform="rotate(-90 44 44)"/><text x="44" y="50" text-anchor="middle">50%</text></svg>
      <h2 class="exam-title">Self-Assesstment 2005</h2>
      <p class="exam-status">63 of 125 answered</p>
      <div class="exam-action"><svg width="30" height="34" viewBox="0 0 30 34"><path d="M9 6H2v26h26V6h-7M15 2v22M8 17l7 7 7-7" fill="none" stroke="var(--icon-blue)" stroke-width="2"/></svg></div>
    </li>
    <li class="exam-card">
      <svg class="progress-ring" viewBox="0 0 88 88"><use href="#ring-base"/><circle cx="44" cy="44" r="39" fill="none" stroke="url(#ring-fill)" stroke-width="7" stroke-dasharray="151.9 245" transform="rotate(-90 44 44)"/><text x="44" y="50" text-anchor="middle">62%</text></svg>
      <h2 class="exam-title">Parathyroid Surgery</h2>
      <p class="exam-status">76 of 125 answered</p>
      <div class="exam-action"><svg width="20" height="32" viewBox="0 0 20 32"><path d="M3 2l14 14L3 30" fill="none" stroke="var(--icon-blue)" stroke-width="2"/></svg></div>
    </li>
    <li class="exam-card">
      <svg class="progress-ring" viewBox="0 0 88 88"><use href="#ring-base"/><circle cx="44" cy="44" r="39" fill="none" stroke="url(#ring-fill)" stroke-width="7"/><text x="44" y="50" text-anchor="middle">100%</text></svg>
      <h2 class="exam-title">Brindle Mobile v1.3</h2>
      <p class="exam-status">Submitted</p>
      <div class="exam-action"><svg width="30" height="34" viewBox="0 0 30 34"><path d="M9 6H2v26h26V6h-7M15 2v22M8 17l7 7 7-7" fill="none" stroke="var(--icon-blue)" stroke-width="2"/></svg></div>
    </li>
    <li class="exam-card">
      <svg class="progress-ring" viewBox="0 0 88 88"><use href="#ring-base"/><circle cx="44" cy="44" r="39" fill="none" stroke="url(#ring-fill)" stroke-width="7" stroke-dasharray="61.3 245" transform="rotate(-90 44 44)"/><text x="44" y="50" text-anchor="middle">25%</text></svg>
      <h2 class="exam-title">Skin and Soft Tissue</h2>
      <p class="exam-status">32 of 125 answered</p>
      <div class="exam-action"><svg width="20" height="32" viewBox="0 0 20 32"><path d="M3 2l14 14L3 30" fill="none" stroke="var(--icon-blue)" stroke-width="2"/></svg></div>
    </li>
    <li class="exam-card">
      <svg class="progress-ring" viewBox="0 0 88 88"><use href="#ring-base"/><circle cx="44" cy="44" r="39" fill="none" stroke="url(#ring-fill)" stroke-width="7" stroke-dasharray="183.8 245" transform="rotate(-90 44 44)"/><text x="44" y="50" text-anchor="middle">75%</text></svg>
      <h2 class="exam-title">Brindle Mobile Advanced Topics 2</h2>
      <p class="exam-status">93 of 125 answered</p>
      <div class="exam-action"><svg width="30" height="34" viewBox="0 0 30 34"><path d="M9 6H2v26h26V6h-7M15 2v22M8 17l7 7 7-7" fill="none" stroke="var(--icon-blue)" stroke-width="2"/></svg></div>
    </li>
    <li class="exam-card">
      <svg class="progress-ring" viewBox="0 0 88 88"><use href="#ring-base"/><circle cx="44" cy="44" r="39" fill="none" stroke="url(#ring-fill)" stroke-width="7" stroke-dasharray="29.4 245" transform="rotate(-90 44 44)"/><text x="44" y="50" text-anchor="middle">12%</text></svg>
      <h2 class="exam-title">Hip Arthrospcopy Essentials</h2>
      <p class="exam-status">15 of 125 answered</p>
      <div class="exam-action"><svg width="30" height="34" viewBox="0 0 30 34"><path d="M9 6H2v26h26V6h-7M15 2v22M8 17l7 7 7-7" fill="none" stroke="var(--icon-blue)" stroke-width="2"/></svg></div>
    </li>
  </ul>
</div>
</body>
</html>
```